Ferncrest Dental, LLC business card project

Business card to be designed with current logo.
Dental office- please keep design of card that looks clean and professional.
Please include the following info:
Ferncrest Dental, LLC
Dr. Lorna Pettigrew
2871 Marlowe Street
Alderbrook, XY 10293
555-555-0193
ferncrestdental.office@examplemail.test
Hello everyone-
Reason: Just got back from overseas- will look at all designs and provide feedback. Thank you!
Reason: Polling my friends for the final selection-
thank you to all those that participated- so many talented designers!

```html
<!DOCTYPE html>
<html lang="en">
<head>
<meta charset="utf-8">
<title>Ferncrest Dental – Business Card</title>
<link rel="stylesheet" href="https://fonts.googleapis.com/css2?family=Noto+Sans:wght@400;500&display=swap">
<style>
  :root {
    --green-deep: #1f6a06;
    --green-mid: #3a9a0a;
    --green-bright: #5de80a;
    --green-brand: #7cc614;
    --name-red: #d3121c;
    --white: #ffffff;
    --divider: #2b5e12;
  }
  html, body {
    margin: 0;
    padding: 0;
    width: 1200px;
    height: 695px;
    overflow: hidden;
    background: var(--green-mid);
  }
  .card {
    position: relative;
    width: 1200px;
    height: 695px;
    overflow: hidden;
    font-family: "Noto Sans", sans-serif;
  }
  .card__left {
    position: absolute;
    left: 0; top: 0;
    width: 601px; height: 695px;
    background:
      radial-gradient(ellipse 420px 300px at 510px 230px, var(--green-bright) 0%, rgba(93,232,10,0) 70%),
      radial-gradient(ellipse 700px 500px at 300px 620px, #3fae10 0%, rgba(63,174,16,0) 70%),
      linear-gradient(160deg, #236f06 0%, #38a50c 55%, #2a8a08 100%);
  }
  .card__right {
    position: absolute;
    left: 603px; top: 0;
    width: 597px; height: 695px;
    background: linear-gradient(180deg, var(--green-bright) 0%, #3c9e0b 22%, var(--green-deep) 50%, #2f8408 68%, #55d40c 100%);
  }
  .card__divider {
    position: absolute;
    left: 598px; top: 0;
    width: 6px; height: 695px;
    background: linear-gradient(90deg, rgba(0,0,0,0.25), var(--divider) 50%, rgba(255,255,255,0.25));
  }
  .name-tab {
    position: absolute;
    left: 174px; top: 253px;
    width: 425px; height: 188px;
    border-radius: 32px 0 0 32px;
    background: linear-gradient(90deg, var(--white) 0%, var(--white) 84%, #d6d6d6 94%, #8a8a8a 100%);
    box-shadow: 0 3px 6px rgba(0,0,0,0.35);
  }
  .name-tab__name {
    position: absolute;
    left: 30px; top: 74px;
    margin: 0;
    font-weight: 500;
    font-size: 33px;
    line-height: 40px;
    letter-spacing: 0.3px;
    color: var(--name-red);
    white-space: nowrap;
  }
  .contact {
    position: absolute;
    left: 640px; top: 262px;
    color: var(--white);
    font-size: 29px;
    line-height: 36px;
    text-shadow: 1px 2px 2px rgba(0,0,0,0.45);
    white-space: nowrap;
  }
  .contact p { margin: 0; }
  .contact__phone { margin-top: 12px !important; }
  .brand {
    position: absolute;
    left: 604px; top: 535px;
    width: 524px; height: 90px;
    background: var(--white);
    display: flex;
    align-items: center;
    justify-content: center;
    gap: 16px;
  }
  .brand__dot {
    width: 22px; height: 22px;
    border-radius: 50%;
    background: var(--green-brand);
  }
  .brand__name {
    font-size: 44px;
    font-weight: 400;
    color: var(--green-brand);
    letter-spacing: -0.5px;
  }
</style>
</head>
<body>
  <div class="card">
    <div class="card__left"></div>
    <div class="card__right"></div>
    <div class="card__divider"></div>

    <div class="name-tab">
      <h1 class="name-tab__name">Dr. Lorna Pettigrew</h1>
    </div>

    <div class="contact">
      <p>2871 Marlowe Street</p>
      <p>Alderbrook, XY 10293</p>
      <p class="contact__phone">555-555-0193</p>
      <p>ferncrestdental.office@examplemail.test</p>
    </div>

    <div class="brand">
      <span class="brand__dot"></span>
      <span class="brand__name">Ferncrest Dental</span>
    </div>
  </div>
</body>
</html>
```